Harbor: Social Media Image: FLU

We are looking to create a social media graphic that can be used. We would like it to mimic this --> https://www.plvo.org/This-is-your-shot_01.png
Will contain the:
-- Campaign Name: HARBOR,
-- Moto: Protect Your Community. Protect Your Elders. Stay Vaccinated.
-- QT7 logo
-- Language: Learn more about getting vaccinated against COVID-19
-- Picture of real person

Please reference our QT7 homepage for visual inspiration qtbridged.org or look here: https://qtbridged.org/resources/dementia-risk-reduction-flyers-healthy-heart-healthy-brain/

```html
<!DOCTYPE html>
<html lang="en">
<head>
<meta charset="utf-8">
<title>Harbor – Stay Vaccinated</title>
<link rel="stylesheet" href="https://fonts.googleapis.com/css2?family=Bebas+Neue&display=swap">
<style>
  :root {
    --cream: #f3e9d8;
    --cream-deep: #eadcc4;
    --clay: #b5564f;
    --teal: #3e9dad;
    --band-dark: #2f7f8c;
    --plum: #8e2f8a;
    --amber: #f0925a;
  }
  * { margin: 0; padding: 0; box-sizing: border-box; }
  html, body { width: 1200px; height: 1200px; overflow: hidden; background: var(--cream); }
  .poster {
    position: relative;
    width: 1200px;
    height: 1200px;
    overflow: hidden;
    background: linear-gradient(180deg, var(--cream) 0%, var(--cream-deep) 100%);
    font-family: "Bebas Neue", "Oswald", sans-serif;
  }
  .border-band {
    position: absolute;
    left: 0;
    width: 1200px;
    height: 56px;
    background: linear-gradient(180deg, var(--cream-deep) 0%, var(--teal) 35%, var(--clay) 65%, var(--cream-deep) 100%);
    opacity: 0.85;
  }
  .border-band--top { top: 0; }
  .border-band--bottom { bottom: 0; }
  .elders-photo {
    position: absolute;
    left: 400px;
    top: 170px;
    width: 800px;
    height: 1000px;
    background:
      radial-gradient(ellipse at 68% 20%, #b79a86 0%, transparent 30%),
      radial-gradient(ellipse at 70% 52%, var(--plum) 0%, transparent 40%),
      radial-gradient(ellipse at 85% 85%, var(--amber) 0%, transparent 40%),
      radial-gradient(ellipse at 40% 80%, #7a2a3a 0%, transparent 45%),
      linear-gradient(160deg, #a88464 0%, #6b3b4a 60%, #c2553a 100%);
    -webkit-mask-image: radial-gradient(ellipse 75% 70% at 68% 62%, #000 65%, transparent 100%);
    mask-image: radial-gradient(ellipse 75% 70% at 68% 62%, #000 65%, transparent 100%);
  }
  .partner-mark {
    position: absolute;
    top: 82px;
    left: 778px;
    display: flex;
    align-items: center;
    gap: 16px;
  }
  .partner-mark__dot {
    width: 100px;
    height: 100px;
    border-radius: 50%;
    border: 5px solid var(--teal);
  }
  .partner-mark__name {
    color: var(--teal);
    font-size: 31px;
    line-height: 1.0;
    letter-spacing: 0.5px;
  }
  .campaign-title {
    position: absolute;
    left: 34px;
    top: 92px;
    color: var(--clay);
    font-size: 250px;
    line-height: 1;
    letter-spacing: 2px;
  }
  .motto {
    position: absolute;
    left: 30px;
    top: 355px;
    list-style: none;
  }
  .motto__item {
    display: flex;
    align-items: center;
    gap: 4px;
    height: 68px;
    margin-bottom: 67px;
    color: var(--teal);
    font-size: 70px;
    line-height: 1;
    letter-spacing: -0.5px;
    word-spacing: -6px;
  }
  .motto__tick { width: 50px; height: 50px; flex: none; }
  .host-mark {
    position: absolute;
    left: 22px;
    bottom: 70px;
    color: var(--clay);
    font-size: 50px;
    line-height: 1.05;
  }
</style>
</head>
<body>
<main class="poster">
  <div class="border-band border-band--top" role="img" aria-label="Woven geometric zigzag border in teal and clay"></div>

  <div class="elders-photo" role="img" aria-label="Photograph of two Native elder women in traditional satin clothing and silver jewelry, one seated wrapped in a patterned blanket"></div>

  <div class="partner-mark">
    <span class="partner-mark__dot"></span>
    <p class="partner-mark__name">Cedar River<br>Resource Center<br>for Mind Health</p>
  </div>

  <h1 class="campaign-title">HARBOR</h1>

  <ul class="motto">
    <li class="motto__item">
      <svg class="motto__tick" viewBox="0 0 50 50" aria-hidden="true"><path d="M6 27 L19 42 L45 8" fill="none" stroke="currentColor" stroke-width="8" stroke-linecap="round" stroke-linejoin="round"/></svg>
      Protect your community.
    </li>
    <li class="motto__item">
      <svg class="motto__tick" viewBox="0 0 50 50" aria-hidden="true"><path d="M6 27 L19 42 L45 8" fill="none" stroke="currentColor" stroke-width="8" stroke-linecap="round" stroke-linejoin="round"/></svg>
      Protect your elders.
    </li>
    <li class="motto__item">
      <svg class="motto__tick" viewBox="0 0 50 50" aria-hidden="true"><path d="M6 27 L19 42 L45 8" fill="none" stroke="currentColor" stroke-width="8" stroke-linecap="round" stroke-linejoin="round"/></svg>
      Stay vaccinated.
    </li>
  </ul>

  <p class="host-mark">QT7 Quiet Tide Alliance<br>for Elder Wellbeing</p>

  <div class="border-band border-band--bottom" role="img" aria-label="Woven geometric zigzag border in teal and clay"></div>
</main>
</body>
</html>
```